Corporate Two Sided Business Card

Looking for a Corporate "edgy" Modern look and feel for a business card

We are looking at two options. Dark background with our logo on it, white background with our logo on it - The background is more - Charcoal / Graphite then black

Details will be

Danielle Forsk

Licensee / Director

m. 0428 519 064

e. danielle@quorvela.com.au

quorvela.com.au

Target Market(s)

Professional Business people that refer use business and clients that own Investment Properties

Industry/Entity Type

Business

Contact Information for Business Card

Details will be

Danielle Forsk

Licensee / Director

m. 0428 519 064

quorvela.com.au

Font styles to use
Serif

Colors
000000
ec1f27
eeeeee
ffffff

Requirements
Must have
• Two options - White Background and Dark Background. - Two sided
Nice to have
• A design that is edgy, modern and new to look instead of boring style corporate cards - It should be a full integrated design
Should not have
• Block looking - Cheap.

```html
<!DOCTYPE html>
<html lang="en">
<head>
<meta charset="utf-8">
<title>Quorvela — Business Card</title>
<link href="https://fonts.googleapis.com/css2?family=Montserrat:wght@400;500;600;700&display=swap" rel="stylesheet">
<style>
  :root {
    --stage: #2b2b2b;
    --charcoal: #343435;
    --paper: #ffffff;
    --red: #ec1f27;
    --graphite: #4a4b4d;
    --ink: #3a3a3a;
    --light: #eeeeee;
  }
  * { margin: 0; padding: 0; box-sizing: border-box; }
  html, body {
    width: 1200px; height: 864px; overflow: hidden;
    background: var(--stage);
    font-family: "Montserrat", sans-serif;
  }
  .stage {
    width: 1200px; height: 864px;
    display: flex; flex-direction: column;
    align-items: center; justify-content: center; gap: 40px;
  }
  .card {
    position: relative;
    width: 660px; height: 377px;
    border-radius: 22px;
    overflow: hidden;
  }
  /* Back side */
  .card--back { background: var(--charcoal); }
  .card--back .wordmark {
    position: absolute; left: 0; right: 0; top: 130px;
    display: flex; justify-content: center; align-items: center; gap: 12px;
    color: var(--paper); font-size: 40px; font-weight: 600; letter-spacing: 1px;
  }
  .mark-square { width: 22px; height: 22px; background: var(--red); }
  .card--back .website {
    position: absolute; left: 0; right: 0; bottom: 62px;
    text-align: center; color: var(--light);
    font-size: 16px; letter-spacing: 1px;
  }
  /* Front side */
  .card--front { background: var(--paper); }
  .card--front .wordmark {
    position: absolute; left: 48px; top: 52px;
    display: flex; align-items: center; gap: 12px;
    color: var(--graphite); font-size: 40px; font-weight: 600; letter-spacing: 1px;
  }
  .card--front .wordmark .mark-square { width: 24px; height: 24px; }
  .feature-block {
    position: absolute; right: 52px; top: 72px;
    width: 220px; height: 220px; background: var(--red);
  }
  .person { position: absolute; left: 48px; top: 190px; }
  .person__name { color: var(--red); font-size: 28px; font-weight: 700; letter-spacing: .5px; }
  .person__role { color: var(--ink); font-size: 17px; font-weight: 500; margin-top: 2px; letter-spacing: .5px; }
  .contacts { position: absolute; left: 48px; top: 272px; list-style: none; }
  .contacts li {
    display: flex; align-items: center; gap: 12px;
    color: var(--ink); font-size: 17px; font-weight: 500; line-height: 27px; letter-spacing: .4px;
  }
  .contacts svg { width: 16px; height: 16px; flex: none; }
</style>
</head>
<body>
<main class="stage">
  <section class="card card--back" aria-label="Card back">
    <div class="wordmark"><span class="mark-square"></span><span>quorvela</span></div>
    <p class="website">www.quorvela.com.au</p>
  </section>

  <section class="card card--front" aria-label="Card front">
    <div class="wordmark"><span class="mark-square"></span><span>quorvela</span></div>
    <div class="feature-block"></div>
    <div class="person">
      <h1 class="person__name">Danielle Forsk</h1>
      <p class="person__role">Licensee / Director</p>
    </div>
    <ul class="contacts">
      <li>
        <svg viewBox="0 0 16 16" aria-hidden="true"><rect x="4" y="1" width="8" height="14" rx="1.5" fill="none" stroke="var(--red)" stroke-width="1.6"/><circle cx="8" cy="12.5" r="0.9" fill="var(--red)"/></svg>
        0428 519 064
      </li>
      <li>
        <svg viewBox="0 0 16 16" aria-hidden="true"><rect x="1" y="3" width="14" height="10" fill="var(--red)"/><path d="M1 3 L8 9 L15 3" fill="none" stroke="#fff" stroke-width="1.3"/></svg>
        danielle@quorvela.com.au
      </li>
      <li>
        <svg viewBox="0 0 16 16" aria-hidden="true"><g fill="none" stroke="var(--red)" stroke-width="1.3"><circle cx="8" cy="8" r="6.5"/><ellipse cx="8" cy="8" rx="3" ry="6.5"/><path d="M1.5 8h13M2.5 4.8h11M2.5 11.2h11"/></g></svg>
        quorvela.com.au
      </li>
    </ul>
  </section>
</main>
</body>
</html>
```